Sophrologist needs a cool signage at door entrance

I need signage for dr in sophrology based in Belgium (french speaking). The signed should capture the name the "Mireille Vantoorn" - "Naturopathe-Sophrologue-Reiki" and a catchphrase = (Healthy way of life)
« Fais du bien à ton corps, pour que ton âme ait envie d’y rester »
Requirements
Must have
- Hey,
Thats the instagram account for some inspiration www.instagram.com/mireille_serene_wellbeing
Light colors, green, blue
Healthy way of life
Size is 45cm wide on 30 cm high
The signage will be placed in front off woof pannel

```html
<!DOCTYPE html>
<html lang="fr">
<head>
<meta charset="utf-8">
<title>Mireille Vantoorn – Signalétique</title>
<link rel="stylesheet" href="https://fonts.googleapis.com/css2?family=Montserrat:wght@300;400;600;700&display=swap">
<style>
  :root {
    --page-bg: #eef1f3;
    --name-blue: #56c3dc;
    --role-green: #8cc63f;
    --band-green: rgba(108, 192, 62, 0.88);
    --tagline-white: #ffffff;
    --sky-top: #ffffff;
    --sky-mid: #e4f3fa;
    --sea: #4fb7d3;
    --sea-deep: #2fa3c4;
    --hill-green: #7cc043;
    --grass-yellow: #d8e27a;
    --portrait-light: #f6d7c4;
    --portrait-mid: #e8b79a;
    --portrait-hair: #8a5a3a;
    --blossom: #f2705a;
  }
  * { margin: 0; padding: 0; box-sizing: border-box; }
  html, body {
    width: 900px;
    height: 1200px;
    overflow: hidden;
    background: var(--page-bg);
  }
  .canvas {
    position: relative;
    width: 900px;
    height: 1200px;
    display: flex;
    align-items: center;
    justify-content: center;
  }
  .sign {
    position: relative;
    width: 900px;
    height: 600px;
    overflow: hidden;
  }
  .sign__scenery, .sign__portrait {
    position: absolute;
    inset: 0;
  }
  .sign__title {
    position: absolute;
    left: 440px;
    right: 0;
    top: 30px;
    text-align: center;
    font-family: "Montserrat", sans-serif;
    color: var(--name-blue);
    line-height: 1;
  }
  .sign__first-name {
    display: block;
    font-weight: 700;
    font-size: 66px;
    letter-spacing: 0.5px;
    margin-left: 8px;
  }
  .sign__last-name {
    display: block;
    font-weight: 300;
    font-size: 66px;
    margin-top: -4px;
    margin-left: 16px;
  }
  .sign__roles {
    position: absolute;
    left: 440px;
    right: 0;
    top: 162px;
    text-align: center;
    font-family: "Montserrat", sans-serif;
    font-weight: 600;
    font-size: 26px;
    line-height: 29px;
    color: var(--role-green);
    margin-left: 0;
  }
  .sign__roles li { list-style: none; }
  .sign__band {
    position: absolute;
    left: 345px;
    right: 0;
    top: 497px;
    height: 68px;
    background: var(--band-green);
  }
  .sign__tagline {
    position: absolute;
    left: 345px;
    right: 0;
    top: 497px;
    height: 68px;
    display: flex;
    align-items: center;
    justify-content: center;
    padding-left: 60px;
    font-family: "Montserrat", sans-serif;
    font-weight: 700;
    font-size: 42px;
    color: var(--tagline-white);
  }
</style>
</head>
<body>
<main class="canvas">
  <section class="sign">
    <svg class="sign__scenery" width="900" height="600" viewBox="0 0 900 600" role="img" aria-label="Photo d'une baie tropicale vue d'une colline, mer turquoise, petits bateaux, verdure et une femme au chapeau de paille fleuri">
      <defs>
        <linearGradient id="scenery-sky" x1="0" y1="0" x2="0" y2="1">
          <stop offset="0" stop-color="var(--sky-top)"/>
          <stop offset="0.4" stop-color="var(--sky-mid)"/>
          <stop offset="0.56" stop-color="var(--sea)"/>
          <stop offset="0.75" stop-color="var(--sea-deep)"/>
          <stop offset="0.85" stop-color="var(--hill-green)"/>
          <stop offset="1" stop-color="var(--grass-yellow)"/>
        </linearGradient>
      </defs>
      <rect width="900" height="600" fill="url(#scenery-sky)"/>
    </svg>
    <svg class="sign__portrait" width="900" height="600" viewBox="0 0 900 600" role="img" aria-label="Photo en forme de feuille d'une femme détendue recevant un massage crânien, fleurs en arrière-plan">
      <defs>
        <linearGradient id="portrait-tones" x1="0.8" y1="0" x2="0.1" y2="1">
          <stop offset="0" stop-color="var(--blossom)" stop-opacity="0.7"/>
          <stop offset="0.3" stop-color="var(--portrait-light)"/>
          <stop offset="0.6" stop-color="var(--portrait-mid)"/>
          <stop offset="1" stop-color="var(--portrait-hair)"/>
        </linearGradient>
      </defs>
      <path d="M440 12 C320 40 80 150 0 250 L0 600 L90 600 C300 470 470 300 440 12 Z" fill="#ffffff" opacity="0.55"/>
      <path d="M438 14 C320 42 80 152 0 252 L0 600 L80 600 C290 470 458 300 438 14 Z" fill="url(#portrait-tones)"/>
    </svg>

    <h1 class="sign__title">
      <span class="sign__first-name">Mireille</span>
      <span class="sign__last-name">Vantoorn</span>
    </h1>
    <ul class="sign__roles">
      <li>Naturopathe</li>
      <li>Sophrologue</li>
      <li>Reiki</li>
    </ul>

    <div class="sign__band"></div>
    <p class="sign__tagline">Healthy way of life</p>
  </section>
</main>
</body>
</html>
```